NOLV.
ENCOMPASSING YOU
NOLV. -
Creative Brief
Use specific fonts
any thing which suits with the LOGO provided
Professional
RAHUL MEHTA
MR.
D-47, NORTH PARK-III, GURGAON 122019, HARYANA, INDIA
rahul@nolv.co
www.nolv.co
use logo at centre

```html
<!DOCTYPE html>
<html lang="en">
<head>
<meta charset="utf-8">
<title>NOLV. Stationery Set</title>
<link rel="stylesheet" href="https://fonts.googleapis.com/css2?family=Roboto:wght@400;700;900&display=swap">
<style>
:root{
  --stage:#333335;
  --paper:#ffffff;
  --red:#d0141c;
  --red-deep:#8e0a10;
  --ink:#4a4a4a;
  --muted:#9a9a9a;
  --faint:rgba(208,20,28,0.07);
  --flap:#3d3d40;
  --envelope-back:#f1f1f1;
  --label:#b8b8b8;
}
*{box-sizing:border-box;margin:0;padding:0}
html,body{width:1200px;height:346px;overflow:hidden}
body{background:var(--stage);font-family:'Roboto',sans-serif;position:relative;color:var(--ink)}
.piece{position:absolute;background:var(--paper);overflow:hidden;box-shadow:0 2px 6px rgba(0,0,0,.35)}
.swoosh{position:absolute;inset:0;width:100%;height:100%}
.brand{position:absolute;display:flex;align-items:center;gap:3px;white-space:nowrap}
.brand-mark{width:8px;height:8px;background:var(--red);flex:none}
.brand-name{color:var(--red);font-weight:900;letter-spacing:.5px;line-height:1}
.tagline{position:absolute;color:var(--muted);font-size:3.5px;letter-spacing:.6px;font-weight:700;white-space:nowrap}
.contact{position:absolute;font-size:3.6px;line-height:6px;color:var(--ink);border-left:.6px solid var(--muted);padding-left:3px;white-space:nowrap}
.ghost{position:absolute;left:50%;top:50%;transform:translate(-50%,-50%);color:var(--faint);font-weight:900;line-height:1}
.footer-line{position:absolute;left:0;right:0;text-align:center;font-size:3.2px;color:var(--muted);white-space:nowrap}
.label{position:absolute;color:var(--label);font-size:5px;white-space:nowrap}
.person{position:absolute;color:var(--red);font-weight:700;font-size:6px;white-space:nowrap}
.person small{display:block;color:var(--muted);font-weight:400;font-size:3.5px;margin-top:1px}
.address{position:absolute;font-size:3.6px;line-height:5.6px;color:var(--ink);white-space:nowrap}
</style>
</head>
<body>

<span class="label" style="left:19px;top:9px">Business Cards</span>

<div class="piece card" style="left:19px;top:19px;width:130px;height:95px">
  <svg class="swoosh" viewBox="0 0 130 95" preserveAspectRatio="none" aria-hidden="true">
    <path d="M112 0 H130 V95 H122 C128 60 124 25 112 0Z" fill="var(--red)"/>
    <path d="M118 0 H130 V95 H126 C130 60 128 25 118 0Z" fill="var(--red-deep)"/>
  </svg>
  <div class="brand" style="left:10px;top:12px"><span class="brand-mark"></span><span class="brand-name" style="font-size:13px">NOLV.</span></div>
  <span class="tagline" style="left:21px;top:28px">ENCOMPASSING YOU</span>
  <div class="contact" style="left:72px;top:12px">hello@nolv.example<br>www.nolv.example<br>ID: nolv.studio</div>
</div>

<div class="piece card" style="left:19px;top:126px;width:130px;height:95px">
  <svg class="swoosh" viewBox="0 0 130 95" preserveAspectRatio="none" aria-hidden="true">
    <path d="M0 80 C30 86 60 92 80 95 H0Z" fill="var(--red)"/>
    <path d="M112 0 H130 V40 C126 22 120 10 112 0Z" fill="var(--red)"/>
  </svg>
  <div class="person" style="left:10px;top:12px">MR. ANAY KAPUR<small>Director</small></div>
  <div class="address" style="left:10px;top:30px">12 SAMPLE ROAD, SECTOR 00<br>GURGAON 000000, HARYANA, INDIA<br>hello@nolv.example</div>
  <div class="brand" style="left:72px;top:58px"><span class="brand-mark"></span><span class="brand-name" style="font-size:12px">NOLV.</span></div>
</div>

<div class="piece card" style="left:19px;top:233px;width:130px;height:88px">
  <svg class="swoosh" viewBox="0 0 130 88" preserveAspectRatio="none" aria-hidden="true">
    <path d="M0 70 C20 78 40 84 55 88 H0Z" fill="var(--red)"/>
    <path d="M100 0 H130 V25 C120 12 112 5 100 0Z" fill="var(--red)"/>
  </svg>
  <div class="brand" style="left:42px;top:36px"><span class="brand-mark"></span><span class="brand-name" style="font-size:14px">NOLV.</span></div>
</div>
<span class="label" style="left:19px;top:326px">Back Side</span>

<div class="piece letterhead" style="left:180px;top:19px;width:192px;height:293px">
  <svg class="swoosh" viewBox="0 0 192 293" preserveAspectRatio="none" aria-hidden="true">
    <path d="M150 0 H192 V30 C180 14 166 5 150 0Z" fill="var(--red)"/>
    <path d="M0 270 C20 280 40 288 60 293 H0Z" fill="var(--red)"/>
  </svg>
  <div class="brand" style="left:14px;top:12px"><span class="brand-mark"></span><span class="brand-name" style="font-size:16px">NOLV.</span></div>
  <span class="tagline" style="left:25px;top:31px">ENCOMPASSING YOU</span>
  <div class="contact" style="left:112px;top:12px">hello@nolv.example<br>www.nolv.example<br>ID: nolv.studio</div>
  <span class="ghost" style="font-size:46px">NOLV.</span>
  <div class="footer-line" style="bottom:10px">12 SAMPLE ROAD, SECTOR 00, GURGAON 000000, HARYANA, INDIA</div>
</div>
<span class="label" style="left:250px;top:326px">Letterhead Page 1</span>

<div class="piece letterhead" style="left:396px;top:19px;width:216px;height:293px">
  <svg class="swoosh" viewBox="0 0 216 293" preserveAspectRatio="none" aria-hidden="true">
    <path d="M170 0 H216 V30 C204 14 188 5 170 0Z" fill="var(--red)"/>
    <path d="M0 270 C22 280 44 288 66 293 H0Z" fill="var(--red)"/>
  </svg>
  <div class="brand" style="left:16px;top:12px"><span class="brand-mark"></span><span class="brand-name" style="font-size:16px">NOLV.</span></div>
  <span class="tagline" style="left:27px;top:31px">ENCOMPASSING YOU</span>
  <div class="contact" style="left:134px;top:12px">hello@nolv.example<br>www.nolv.example<br>ID: nolv.studio</div>
  <span class="ghost" style="font-size:50px">NOLV.</span>
  <div class="footer-line" style="bottom:10px">12 SAMPLE ROAD, SECTOR 00, GURGAON 000000, HARYANA, INDIA</div>
</div>
<span class="label" style="left:476px;top:326px">Letterhead Page 2</span>

<div class="piece slip" style="left:636px;top:29px;width:228px;height:115px">
  <svg class="swoosh" viewBox="0 0 228 115" preserveAspectRatio="none" aria-hidden="true">
    <path d="M190 0 H228 V28 C216 14 204 5 190 0Z" fill="var(--red)"/>
    <path d="M0 95 C20 104 40 110 60 115 H0Z" fill="var(--red)"/>
  </svg>
  <div class="brand" style="left:12px;top:12px"><span class="brand-mark"></span><span class="brand-name" style="font-size:13px">NOLV.</span></div>
  <span class="tagline" style="left:23px;top:28px">ENCOMPASSING YOU</span>
  <div class="contact" style="left:150px;top:14px">hello@nolv.example<br>www.nolv.example</div>
  <span class="ghost" style="font-size:30px">NOLV.</span>
</div>
<span class="label" style="left:720px;top:150px">Compliment Slip</span>

<div class="piece slip" style="left:636px;top:197px;width:228px;height:115px">
  <svg class="swoosh" viewBox="0 0 228 115" preserveAspectRatio="none" aria-hidden="true">
    <path d="M190 0 H228 V28 C216 14 204 5 190 0Z" fill="var(--red)"/>
    <path d="M0 95 C20 104 40 110 60 115 H0Z" fill="var(--red)"/>
  </svg>
  <div class="brand" style="left:12px;top:12px"><span class="brand-mark"></span><span class="brand-name" style="font-size:13px">NOLV.</span></div>
  <span class="tagline" style="left:23px;top:28px">ENCOMPASSING YOU</span>
  <span class="ghost" style="font-size:30px">NOLV.</span>
  <div class="footer-line" style="bottom:8px">12 SAMPLE ROAD, GURGAON 000000 · hello@nolv.example · www.nolv.example</div>
</div>
<span class="label" style="left:720px;top:318px">Compliment Slip</span>

<div class="piece envelope" style="left:876px;top:29px;width:312px;height:100px">
  <svg class="swoosh" viewBox="0 0 312 100" preserveAspectRatio="none" aria-hidden="true">
    <polygon points="0,0 312,0 156,58" fill="var(--flap)"/>
    <polygon points="0,100 156,48 312,100" fill="var(--envelope-back)"/>
  </svg>
  <div class="brand" style="left:136px;top:14px"><span class="brand-mark"></span><span class="brand-name" style="font-size:11px">NOLV.</span></div>
</div>

<div class="piece envelope" style="left:876px;top:140px;width:312px;height:80px">
  <svg class="swoosh" viewBox="0 0 312 80" preserveAspectRatio="none" aria-hidden="true">
    <polygon points="0,0 312,0 156,50" fill="var(--red)"/>
    <polygon points="0,80 156,40 312,80" fill="var(--envelope-back)"/>
  </svg>
  <div class="brand" style="left:138px;top:12px"><span class="brand-mark" style="background:var(--paper)"></span><span class="brand-name" style="font-size:10px;color:var(--paper)">NOLV.</span></div>
</div>

<div class="piece envelope" style="left:876px;top:232px;width:312px;height:80px">
  <svg class="swoosh" viewBox="0 0 312 80" preserveAspectRatio="none" aria-hidden="true">
    <path d="M270 0 H312 V22 C300 10 286 3 270 0Z" fill="var(--red)"/>
    <path d="M0 66 C20 72 40 77 60 80 H0Z" fill="var(--red)"/>
  </svg>
  <div class="brand" style="left:138px;top:52px"><span class="brand-mark"></span><span class="brand-name" style="font-size:10px">NOLV.</span></div>
</div>

</body>
</html>
```